New Architectural Firm Business Cards

New Business card to compliment previous pixel forum logo (attached). Please design a business card that is simple, modern, creative....please do not use "symbols", simply the logo and associated graphics/text. The front should contain name/address/phone/email/web address (with graphics).....back should be 100% graphic design using the logo somehow. Hoping for a two color (black and yellow) design. full bleed design, no borders

Target Market(s)

Commercial Architecture Clients

Industry/Entity Type

Architecture

Contact Information for Business Card

Please design a business card that is simple, modern, creative....please do not use "symbols", simply the logo and associated graphics/text. The front should contain name/address/phone/email/web address (with graphics).....back should be 100% graphic design using the logo somehow

Font styles to use
Sans Serif

Colors
FFF300
FFF600
FEFA6F
FFFEC7
FFFEE8

Requirements
Must have
• Clean, Modern Design
Should not have
• Stock images or "icons"

```html
<!DOCTYPE html>
<html lang="en">
<head>
<meta charset="utf-8">
<title>Pixel Forum Architecture – Business Cards</title>
<link rel="stylesheet" href="https://fonts.googleapis.com/css2?family=Montserrat:wght@300;400;500&display=swap">
<style>
  :root {
    --yellow-strong: #FFF300;
    --yellow-mid: #FEFA6F;
    --yellow-pale: #FFFEC7;
    --yellow-white: #FFFEE8;
    --ink: #1c1c1c;
    --ink-soft: #3a3a3a;
    --card-dark: #2b2b2d;
    --card-darker: #1d1d1f;
    --strip: #161617;
    --white: #f4f4f4;
    --backdrop: #d9d9d9;
  }
  * { margin: 0; padding: 0; box-sizing: border-box; }
  html, body {
    width: 1200px; height: 900px; overflow: hidden;
    background: var(--backdrop);
    font-family: "Montserrat", sans-serif;
  }
  .sheet {
    position: relative; width: 1200px; height: 900px;
    display: flex; flex-direction: column; align-items: center; justify-content: center;
    gap: 60px;
  }
  .card {
    position: relative; width: 600px; height: 343px; overflow: hidden;
  }

  /* Front: contact side */
  .card--front {
    background: linear-gradient(160deg, var(--yellow-pale) 0%, var(--yellow-white) 55%, var(--yellow-pale) 100%);
  }
  .front-wash {
    position: absolute; left: 0; top: 0; width: 420px; height: 190px;
    background: linear-gradient(100deg, var(--yellow-strong) 0%, var(--yellow-mid) 60%, rgba(254,250,111,0) 100%);
    border-bottom-right-radius: 190px;
    opacity: .75;
  }
  .contact {
    position: absolute; right: 44px; bottom: 34px; text-align: right; color: var(--ink);
  }
  .contact__name {
    font-weight: 400; font-size: 34px; letter-spacing: 1px; line-height: 1;
  }
  .contact__role {
    font-weight: 400; font-size: 13px; letter-spacing: 1.5px; margin-top: 4px; margin-bottom: 14px;
  }
  .contact__line {
    font-weight: 300; font-size: 16px; line-height: 1.35; color: var(--ink-soft);
  }

  /* Back: brand side */
  .card--back {
    background: linear-gradient(170deg, var(--card-darker) 0%, var(--card-dark) 60%, #3a3a3c 100%);
  }
  .brand {
    position: absolute; left: 110px; top: 70px; display: flex; flex-direction: column; gap: 10px;
  }
  .brand__row { display: flex; align-items: center; gap: 14px; }
  .brand__mark { width: 34px; height: 34px; background: var(--yellow-strong); }
  .brand__name {
    font-weight: 500; font-size: 46px; color: var(--yellow-strong); line-height: 1;
  }
  .brand__sub {
    font-weight: 300; font-size: 26px; letter-spacing: 1px; color: var(--white);
    padding-left: 48px;
  }
  .web-strip {
    position: absolute; right: 0; bottom: 70px; padding: 8px 36px 8px 28px;
    background: var(--strip);
    font-weight: 300; font-size: 22px; letter-spacing: 1px; color: var(--white);
  }
</style>
</head>
<body>
  <main class="sheet">
    <section class="card card--front" aria-label="Business card front">
      <div class="front-wash"></div>
      <div class="contact">
        <p class="contact__name">ADA MARLOW</p>
        <p class="contact__role">ARCHITECT</p>
        <p class="contact__line">Harbor Lane, 418</p>
        <p class="contact__line">Brooklyn, New York</p>
        <p class="contact__line">(212) 555-0148</p>
        <p class="contact__line">ada@pixelforum-arch.com</p>
      </div>
    </section>

    <section class="card card--back" aria-label="Business card back">
      <div class="brand">
        <div class="brand__row">
          <span class="brand__mark"></span>
          <span class="brand__name">Pixel Forum</span>
        </div>
        <span class="brand__sub">ARCHITECTURE</span>
      </div>
      <p class="web-strip">www.pixelforum-arch.com</p>
    </section>
  </main>
</body>
</html>
```